Form Crafters Business Card

Professional cosmetic surgery company, based in very exclusive area in London. High profiled clientele. Brand is very artistic, modern, state-of-the-art, safe. The best in the business. Celebrity clientele.

Form Crafter’s of London is a brand serving a discriminating and exclusive clientele who value personal service that is both intimate and high end. Our clients choose Form Crafters because of the relationships we share with all of our customers. The clients of Form Crafters have an equal partnership between customers, and very experienced, highly qualified medical professionals. This together provides you with a professional service that keeps you looking good and feeling good. It is a relationship based on honesty, compassion, loyalty and respect.
Form Crafter’s have provided services for internationally recognised celebrities, and other high profiled individuals.

The cards are used for networking at private, exclusive events with VIPs.

Target Market(s)

Professionals
Rich people

Industry/Entity Type

Professional Service

Contact Information for Business Card

Need double sided business card design for 4 people. Back of the business card needs to have contrast background to the front with butterfly watermark with services provided:
Hair Restoration surgery
Hair Loss treatments
Breast surgery
Rhinoplasty
Zelix Liposuction
Fat Grafting
Lumex & Fillers

Front of the business card needs to be a nice satin black.
with following information:
Talvan Desoruthy - name
Chief Executive - Job title

www.formcrafters-example.co.uk
talvan@formcrafters-example.co.uk
Phone: +44 (0)207 146 5327
Mobile: +44 (0)7491 825 436

The London Calder Infirmary
14 Pellmont Street | London | W1K 3TR
Off Dunmore Lane

All business cards have the same address, phone, website as Talvan's details.
Same details on the back of the business card as well.
The other cards have different name, job title, email, mobile number

Kerem Lutz - Name
Partner - Job Title
Former England International Cricketer - please include below job title

email: kerem@formcrafters-example.co.uk
mobile: +44(0)7862 514208

Dr Stellan Vastrel - Name
Plastic Surgeon - Job Title
drvastrel@formcrafters-example.co.uk
No mobile number

Dr Jon Torvick FRCS (please put FRCS in small font) - Name
Hair Restoration Surgeon - Job Title
drtorvick@formcrafters-example.co.uk
No mobile number

Colors
cedeec
85abd2
0655a3

Requirements
Must have
• The logo needs to be in a metallic finish
• Text needs to be striking
• nice background
• butterfly watermark on the back

```html
<!DOCTYPE html>
<html lang="en">
<head>
<meta charset="utf-8">
<title>Form Crafters Business Card</title>
<link href="https://fonts.googleapis.com/css2?family=Cinzel:wght@400;700&display=swap" rel="stylesheet">
<style>
  :root {
    --backdrop: #e9e9ea;
    --satin-black: #1f2022;
    --satin-black-deep: #161719;
    --brand-blue: #2f8fd0;
    --brand-blue-deep: #0655a3;
    --brand-blue-soft: #85abd2;
    --brand-orange: #f06a1f;
    --brand-amber: #f4a13a;
    --silver: #c9cccf;
    --silver-soft: #e4e6e8;
  }
  * { box-sizing: border-box; margin: 0; padding: 0; }
  html, body {
    width: 1200px; height: 720px; overflow: hidden;
    background: var(--backdrop);
    font-family: "Cinzel", serif;
  }
  .canvas {
    position: relative; width: 1200px; height: 720px;
    display: flex; justify-content: center; align-items: center; gap: 40px;
  }
  .card {
    position: relative; width: 540px; height: 309px; overflow: hidden;
    background: linear-gradient(135deg, var(--satin-black) 0%, var(--satin-black-deep) 100%);
  }

  /* Front */
  .watermark {
    position: absolute; top: 0; right: 55px; width: 130px; height: 150px;
    background: radial-gradient(ellipse at center, rgba(120,110,100,.22) 0%, rgba(60,60,70,.08) 60%, transparent 80%);
  }
  .brand {
    position: absolute; display: flex; align-items: center; gap: 10px;
    font-weight: 400; letter-spacing: .5px;
  }
  .front .brand { left: 20px; top: 58px; font-size: 28px; color: var(--brand-blue); }
  .brand-dot { width: 14px; height: 14px; border-radius: 50%; background: currentColor; }
  .person {
    position: absolute; right: 20px; top: 118px; text-align: right;
  }
  .person-name {
    font-weight: 700; font-size: 17px; letter-spacing: .3px;
    color: var(--brand-orange); text-transform: uppercase;
  }
  .person-title { font-size: 12.5px; color: var(--brand-blue); margin-top: 1px; }
  .divider {
    position: absolute; left: 21px; right: 20px; top: 172px; height: 1.5px;
    background: linear-gradient(90deg, var(--brand-orange), var(--brand-amber) 60%, var(--brand-orange));
  }
  .address, .contacts {
    position: absolute; top: 191px; font-size: 11.5px; line-height: 15.5px;
    color: var(--brand-blue);
  }
  .address { left: 20px; }
  .contacts { right: 20px; text-align: right; }
  .contact-line { display: flex; justify-content: flex-end; align-items: center; gap: 9px; }
  .contact-icon { width: 12px; height: 12px; flex: none; }
  .swoosh { position: absolute; inset: 0; width: 540px; height: 309px; }

  /* Back */
  .back .brand {
    left: 0; right: 0; top: 105px; justify-content: center;
    font-size: 34px; color: var(--silver);
  }
  .services {
    position: absolute; left: 0; right: 0; top: 219px; text-align: center;
    font-size: 12px; line-height: 15.5px; color: var(--silver-soft);
  }
</style>
</head>
<body>
<main class="canvas">

  <section class="card front" aria-label="Business card front">
    <div class="watermark" role="img" aria-label="Faint brand watermark"></div>
    <div class="brand"><span class="brand-dot"></span>Form Crafters</div>

    <div class="person">
      <div class="person-name">Talvan Desoruthy</div>
      <div class="person-title">Chief Executive</div>
    </div>

    <div class="divider"></div>

    <address class="address" style="font-style:normal">
      The London Calder Infirmary<br>
      14 Pellmont Street | London |<br>
      W1K 3TR Off Dunmore Lane
    </address>

    <div class="contacts">
      <div class="contact-line">+44 (0)207 146 5327
        <svg class="contact-icon" viewBox="0 0 12 12"><path d="M1 4 Q6 0 11 4 L10 5.5 L8 4.5 L8 3.5 Q6 3 4 3.5 L4 4.5 L2 5.5 Z M3 6 H9 L10 11 H2 Z" fill="var(--brand-orange)"/></svg>
      </div>
      <div class="contact-line">+44 (0)7491 825 436
        <svg class="contact-icon" viewBox="0 0 12 12"><rect x="3" y="0.8" width="6" height="10.4" rx="1" fill="none" stroke="var(--brand-orange)" stroke-width="1.3"/></svg>
      </div>
      <div class="contact-line">talvan@formcrafters-example.co.uk
        <svg class="contact-icon" viewBox="0 0 12 12"><rect x="0.5" y="2" width="11" height="8" fill="var(--brand-orange)"/><path d="M0.5 2 L6 6.5 L11.5 2" fill="none" stroke="var(--satin-black)" stroke-width="1"/></svg>
      </div>
      <div class="contact-line">www.formcrafters-example.co.uk
        <svg class="contact-icon" viewBox="0 0 12 12"><rect x="1" y="2" width="10" height="7" rx="1" fill="none" stroke="var(--brand-orange)" stroke-width="1.3"/><path d="M4 11 H8" stroke="var(--brand-orange)" stroke-width="1.3"/></svg>
      </div>
    </div>

    <svg class="swoosh" viewBox="0 0 540 309" aria-hidden="true">
      <defs>
        <linearGradient id="swoosh-orange" x1="0" x2="1" y1="0" y2="0">
          <stop offset="0" stop-color="#e8401c"/>
          <stop offset="1" stop-color="#f5a03a"/>
        </linearGradient>
        <linearGradient id="swoosh-blue" x1="0" x2="1" y1="0" y2="0">
          <stop offset="0" stop-color="#0655a3"/>
          <stop offset=".6" stop-color="#2f8fd0"/>
          <stop offset="1" stop-color="#3a86c8"/>
        </linearGradient>
      </defs>
      <path d="M0 236 C40 278 150 298 248 279 C160 304 60 306 0 300 Z" fill="url(#swoosh-orange)"/>
      <path d="M0 309 L0 301 C120 308 230 268 340 260 C430 254 490 262 540 272 L540 309 Z" fill="url(#swoosh-blue)"/>
      <path d="M0 300 C120 307 230 267 340 259 C430 253 490 261 540 271" fill="none" stroke="#0e0f10" stroke-width="2"/>
    </svg>
  </section>

  <section class="card back" aria-label="Business card back">
    <div class="brand"><span class="brand-dot"></span>Form Crafters</div>
    <div class="services">
      Hair Restoration surgery<br>
      Hair Loss treatments<br>
      Breast surgery Rhinoplasty Zelix<br>
      Liposuction Fat Grafting Lumex &amp; Fillers
    </div>
  </section>

</main>
</body>
</html>
```